Tranquil Pathway Business Card

Logo attached. (will be printing onto thick white/off white textured card)

Double sided business card for two Therapists working at Tranquil Pathway.

Require one design, but with different name and mobile numbers on each card.

Target Market(s)

Medical, Health

Industry/Entity Type

Business

Contact Information for Business Card

Need one business card design, but a separate card for each person - Colin Marchetti and Marieke de Boeckx.

FRONT OF CARD

Logo

Name (Colin Marchetti on one card, Marieke de Boeckx on the other)
Professional Clinical Hypnotherapist

Consulting Rooms (Near Lindqvist Hospital)
482 Brackenfield Road
Dunmore VIC 3987

Colin@TranquilPathway.example.au OR Marieke@TranquilPathway.example.au

Mobile: 0455 872 604 (for Colin) OR
Mobile: 0467 290 518 (for Marieke)

BACK OF CARD

Logo

Website: www.TranquilPathway.example.au

Phone: 1300 958 471

Requirements
Must have
• Text and logo only. No additiional graphics.

```html
<!DOCTYPE html>
<html lang="en">
<head>
<meta charset="utf-8">
<title>Tranquil Pathway Business Card</title>
<link rel="stylesheet" href="https://fonts.googleapis.com/css2?family=Montserrat:wght@600&family=Open+Sans:wght@400;600&display=swap">
<style>
  :root {
    --backdrop: #e6e7ea;
    --card: #fbfbfc;
    --navy: #23264f;
    --navy-deep: #14173a;
    --swoosh: #3c3d45;
    --silver: #c9ccd6;
    --ink: #3a3e48;
    --name: #d8ccb4;
    --detail: #e8e8ee;
    --address: #b9ac98;
  }
  * { margin: 0; padding: 0; box-sizing: border-box; }
  html, body { width: 1200px; height: 969px; overflow: hidden; }
  body {
    background: var(--backdrop);
    position: relative;
    font-family: "Open Sans", Arial, sans-serif;
  }
  .business-card {
    position: absolute;
    left: 100px; top: 196px;
    width: 1000px; height: 576px;
    border-radius: 22px;
    background: var(--card);
    overflow: hidden;
    box-shadow: 0 10px 30px rgba(0,0,0,0.12);
  }
  .card-wave { position: absolute; inset: 0; width: 100%; height: 100%; }
  .brand {
    position: absolute; left: 43px; top: 40px;
    display: flex; align-items: center; gap: 26px;
  }
  .brand-mark {
    width: 144px; height: 144px; border-radius: 50%;
    background: var(--swoosh);
  }
  .brand-name {
    font-family: "Montserrat", Arial, sans-serif;
    font-weight: 600; color: var(--ink);
    font-size: 40px; line-height: 1.05; letter-spacing: 1px;
    text-transform: uppercase;
  }
  .contact {
    position: absolute; right: 36px; top: 248px;
    text-align: right; color: var(--detail);
  }
  .person-name {
    font-size: 32px; font-weight: 600; color: var(--name);
    letter-spacing: 1.5px; text-transform: uppercase; line-height: 1.2;
  }
  .person-role { font-size: 23px; color: var(--detail); margin-top: 4px; }
  .contact-list { list-style: none; margin-top: 18px; }
  .contact-list li {
    display: flex; justify-content: flex-end; align-items: center;
    gap: 14px; font-size: 22px; line-height: 39px;
  }
  .contact-list svg { width: 22px; height: 22px; fill: none; stroke: var(--detail); stroke-width: 2; }
  .address { margin-top: 14px; margin-right: 36px; font-size: 22px; line-height: 33px; color: var(--address); }
  .address .street { color: var(--detail); }
</style>
</head>
<body>
  <section class="business-card" aria-label="Tranquil Pathway business card">
    <svg class="card-wave" viewBox="0 0 1000 576" preserveAspectRatio="none" aria-hidden="true">
      <defs>
        <linearGradient id="navyFill" x1="0" y1="0" x2="1" y2="1">
          <stop offset="0" stop-color="#2e3263"/>
          <stop offset="1" stop-color="#14173a"/>
        </linearGradient>
      </defs>
      <path d="M0 405 C 190 430, 320 360, 440 250 S 760 60, 1000 70 L1000 82 C 780 78, 620 170, 470 285 S 180 470, 0 440 Z" fill="var(--swoosh)"/>
      <path d="M0 470 C 210 480, 340 390, 470 280 S 780 92, 1000 84 L1000 576 L0 576 Z" fill="var(--silver)"/>
      <path d="M0 478 C 215 488, 345 398, 476 288 S 785 100, 1000 94 L1000 576 L0 576 Z" fill="url(#navyFill)"/>
    </svg>

    <div class="brand">
      <div class="brand-mark" aria-hidden="true"></div>
      <div class="brand-name">Tranquil<br>Pathway</div>
    </div>

    <div class="contact">
      <h1 class="person-name">Colin Marchetti</h1>
      <p class="person-role">Professional Clinical Hypnotherapist</p>
      <ul class="contact-list">
        <li>0455 872 604
          <svg viewBox="0 0 24 24" aria-hidden="true"><rect x="7" y="2" width="10" height="20" rx="2"/><line x1="11" y1="18" x2="13" y2="18"/></svg>
        </li>
        <li>Colin@TranquilPathway.example.au
          <svg viewBox="0 0 24 24" aria-hidden="true"><rect x="3" y="6" width="18" height="12"/><polyline points="3,6 12,13 21,6"/></svg>
        </li>
        <li>www.TranquilPathway.example.au
          <svg viewBox="0 0 24 24" aria-hidden="true"><circle cx="12" cy="12" r="9"/><ellipse cx="12" cy="12" rx="4" ry="9"/><line x1="3" y1="12" x2="21" y2="12"/></svg>
        </li>
      </ul>
      <p class="address">Consulting Rooms (Near Lindqvist Hospital)<br><span class="street">482 Brackenfield Road, Dunmore VIC 3987</span></p>
    </div>
  </section>
</body>
</html>
```